DRONE FLYERS.: : Presentation of the Vireo Rotorcraft Drone Division Vireo Rotorcraft has ...

- 1-Service to mining companies•Volumetric/Photogrammetry• Geophysical surveys•Mapping•Inspections-2- Visual and / or thermal inspections• Power lines•Pipelines/pipelines• Railroads-3- Services to municipalities•Planning• Various inspections• Civil security-4- Agricultural -55service•Multispectral•Mapping•Volumetric/Photogrammetry

```html
<!DOCTYPE html>
<html lang="en">
<head>
<meta charset="utf-8">
<title>Vireo Rotorcraft Drone Division – Trifold Brochure</title>
<link rel="stylesheet" href="https://fonts.googleapis.com/css2?family=Oswald:wght@500&family=Roboto+Condensed:wght@400&family=Open+Sans:wght@300;400;600;700&display=swap">
<style>
:root{
  --page:#d5d5d7;
  --ink:#1c1c1c;
  --dark:#1a1a1a;
  --paper:#ffffff;
  --blue:#5b9bd5;
  --blue-deep:#2f7fc4;
}
*{box-sizing:border-box;margin:0;padding:0}
html,body{width:858px;height:1200px;overflow:hidden;background:var(--page)}
body{position:relative;font-family:"Open Sans",sans-serif;color:var(--ink)}
.sheet{position:absolute;left:57px;width:749px;height:530px;overflow:hidden;box-shadow:0 10px 14px rgba(0,0,0,.28)}
.sheet--outside{top:53px}
.sheet--inside{top:632px}
.sheet-bg{position:absolute;inset:0}
.abs{position:absolute}
.title{font-family:"Oswald",sans-serif;font-weight:500;font-size:14px;letter-spacing:.2px;text-transform:uppercase}
.title--light{color:var(--paper)}
.title-rule{position:absolute;height:1px;background:#9aa}
.cond{font-family:"Roboto Condensed",sans-serif}
.photo{position:absolute;overflow:hidden}
.ring{border-radius:50%;border:5px solid #cfd8e2;box-shadow:0 0 0 1px rgba(0,0,0,.15)}

.service-list{list-style:none;position:absolute;left:26px;top:56px}
.service-list li{display:flex;align-items:center;height:25px;font-size:11px}
.service-list svg{margin-right:6px;flex:none}
.mining{position:absolute;left:20px;top:430px;color:var(--paper)}
.mining h3{font-family:"Oswald",sans-serif;font-weight:500;font-size:7.5px;margin-bottom:8px;white-space:nowrap}
.mining ul{list-style:none;position:absolute;top:16px;width:120px}
.mining li{font-size:6.4px;line-height:10px;white-space:nowrap}
.mining li::before{content:"";display:inline-block;width:4px;height:4px;border:1px solid var(--blue);border-radius:50%;margin-right:4px;vertical-align:0}

.about{position:absolute;left:267px;top:135px;width:215px;color:var(--paper)}
.about h2{text-align:center;margin-bottom:10px}
.about p{font-size:8.9px;line-height:11.6px;text-align:justify}
.contact{position:absolute;left:262px;top:396px;width:225px;color:var(--paper);text-align:center}
.contact h2{margin-bottom:10px}
.contact p{font-size:7.3px;line-height:11px}
.contact strong{font-weight:700}

.brand{position:absolute;left:517px;top:22px;display:flex;align-items:center}
.brand-mark{width:46px;height:46px;border-radius:50%;border:2px solid #333;margin-right:18px;flex:none}
.brand-name{font-weight:300;color:var(--ink);line-height:1.15;white-space:nowrap}
.brand-name .small{display:block;font-size:10.5px;letter-spacing:1.3px}
.brand-name .big{display:block;font-size:19px}
.tagline{position:absolute;left:504px;top:436px;width:240px;text-align:center;color:var(--paper);font-size:13.5px;line-height:22px}
.url-pill{position:absolute;left:517px;top:491px;width:219px;height:22px;border-radius:11px;background:var(--paper);color:var(--ink);font-size:11px;line-height:22px;text-align:center;box-shadow:0 2px 4px rgba(0,0,0,.4)}

.photogrammetry{position:absolute;left:0;top:0;width:250px;height:530px;color:var(--paper)}
.photogrammetry h2{position:absolute;left:20px;top:24px}
.lead{position:absolute;font-size:9.6px}
.ticks{list-style:none;position:absolute;left:20px;top:170px;width:220px}
.ticks li{font-size:9.4px;line-height:16px;padding-left:13px;position:relative}
.ticks li::before{content:"";position:absolute;left:0;top:5px;width:5px;height:5px;border:1.5px solid var(--blue);border-radius:50%}

.volumetric h2{position:absolute;left:250px;top:24px;width:250px;text-align:center;color:var(--ink)}
.calc{position:absolute;left:266px;top:84px;width:90px;font-size:5.4px;line-height:7px;color:#222}
.calc b{font-size:6.8px;display:block;margin-bottom:12px}
.calc p{margin-bottom:10px}
.feature-list{list-style:none;position:absolute;left:272px;top:211px}
.feature-list li{display:flex;align-items:center;height:32px;font-size:9.8px;color:#333}
.feature-list svg{margin-right:10px}
.table{position:absolute;top:363px;width:60px;font-size:4.6px;line-height:13px;color:#555}
.table b{font-size:5.6px;color:#222;display:block;line-height:8px}
.footer-bar{position:absolute;left:250px;top:499px;width:499px;height:22px;background:var(--blue);color:var(--paper);font-size:11px;line-height:22px}
.footer-bar .phone{position:absolute;left:90px;display:flex;align-items:center}
.footer-bar .web{position:absolute;left:330px}

.inspection{color:var(--paper)}
.inspection h2{position:absolute;left:527px;top:184px}
.icon-label{position:absolute;width:80px;text-align:center;font-size:8.8px;line-height:10px;color:var(--paper)}
.zoom-tag{position:absolute;left:2px;top:2px;background:rgba(255,255,255,.85);color:#000;font-size:7px;font-weight:700;padding:0 2px}
</style>
</head>
<body>

<section class="sheet sheet--outside" aria-label="Brochure outside">
  <svg class="sheet-bg" width="749" height="530" viewBox="0 0 749 530">
    <defs>
      <linearGradient id="paperGrad" x1="0" y1="0" x2="1" y2="0">
        <stop offset="0" stop-color="#ffffff"/><stop offset="1" stop-color="#dcdcdf"/>
      </linearGradient>
      <linearGradient id="darkGrad" x1="0" y1="0" x2="0" y2="1">
        <stop offset="0" stop-color="#2a2a2c"/><stop offset=".55" stop-color="#38383a"/><stop offset="1" stop-color="#151515"/>
      </linearGradient>
      <linearGradient id="midGrad" x1="0" y1="0" x2="1" y2="1">
        <stop offset="0" stop-color="#1b1b1c"/><stop offset=".5" stop-color="#444446"/><stop offset="1" stop-color="#1c1c1d"/>
      </linearGradient>
      <linearGradient id="droneGrad" x1="0" y1="0" x2="0" y2="1">
        <stop offset="0" stop-color="#8a98ad"/><stop offset=".6" stop-color="#596274"/><stop offset="1" stop-color="#9aa2ad"/>
      </linearGradient>
    </defs>
    <rect x="0" y="0" width="250" height="530" fill="url(#paperGrad)"/>
    <rect x="250" y="0" width="250" height="530" fill="url(#midGrad)"/>
    <rect x="500" y="0" width="249" height="530" fill="url(#darkGrad)"/>
    <path d="M500 0H749V80C690 80 600 88 500 100Z" fill="#ffffff"/>
    <path d="M500 100C600 88 690 80 749 80V290C690 350 600 385 500 390Z" fill="url(#droneGrad)" role="img" aria-label="Photo of a quadcopter drone with a camera gimbal standing on a deck"/>
    <path d="M0 400C40 345 160 320 250 328V530H0Z" fill="#1c1c1d"/>
    <path d="M0 470C10 440 60 395 130 365C170 350 220 345 250 345V332C180 330 80 360 0 430Z" fill="#ffffff" opacity=".9"/>
    <path d="M0 400C40 345 160 320 250 328V336C160 330 40 360 0 420Z" fill="var(--blue)"/>
    <path d="M250 345C380 360 470 395 560 400C640 405 710 370 749 330V350C710 395 640 420 560 418C470 415 380 375 250 360Z" fill="var(--blue)"/>
    <path d="M250 336C380 345 470 380 560 390C640 397 710 360 749 310V330C710 380 640 408 560 404C470 398 380 360 250 345Z" fill="#d8dde4" opacity=".85"/>
  </svg>

  <div class="title abs" style="left:20px;top:26px;color:var(--ink)">Services</div>
  <div class="title-rule" style="left:20px;top:47px;width:120px"></div>
  <ul class="service-list cond">
    <li><svg width="20" height="20" viewBox="0 0 20 20"><circle cx="10" cy="10" r="10" fill="var(--blue-deep)"/><rect x="5" y="7" width="10" height="7" rx="1" fill="#fff"/><circle cx="10" cy="10.5" r="2" fill="var(--blue-deep)"/></svg>PHOTOGRAMMETRY</li>
    <li><svg width="20" height="20" viewBox="0 0 20 20"><circle cx="10" cy="10" r="10" fill="var(--blue-deep)"/><path d="M5 7l5-2 5 2v6l-5 2-5-2z" fill="none" stroke="#fff" stroke-width="1.3"/></svg>VOLUMETRY</li>
    <li><svg width="20" height="20" viewBox="0 0 20 20"><circle cx="10" cy="10" r="10" fill="var(--blue-deep)"/><circle cx="10" cy="8" r="2.6" fill="#fff"/><path d="M5 15c1-3 9-3 10 0z" fill="#fff"/></svg>INSPECTION</li>
    <li><svg width="20" height="20" viewBox="0 0 20 20"><circle cx="10" cy="10" r="10" fill="var(--blue-deep)"/><path d="M10 4a3 3 0 0 1 3 3c0 2-3 6-3 6s-3-4-3-6a3 3 0 0 1 3-3z" fill="#fff"/><path d="M5 15h10" stroke="#fff" stroke-width="1.3"/></svg>CARTOGRAHHIE</li>
    <li><svg width="20" height="20" viewBox="0 0 20 20"><circle cx="10" cy="10" r="10" fill="var(--blue-deep)"/><rect x="6" y="4.5" width="8" height="11" rx="1" fill="none" stroke="#fff" stroke-width="1.3"/><path d="M8 12l4-4" stroke="#fff" stroke-width="1.3"/></svg>SLOPE &amp; CURVE LEVEL</li>
    <li><svg width="20" height="20" viewBox="0 0 20 20"><circle cx="10" cy="10" r="10" fill="var(--blue-deep)"/><path d="M8 6l6 4-6 4z" fill="#fff"/></svg>3D PLAN</li>
    <li><svg width="20" height="20" viewBox="0 0 20 20"><circle cx="10" cy="10" r="10" fill="var(--blue-deep)"/><rect x="6" y="5" width="8" height="10" rx="1" fill="none" stroke="#fff" stroke-width="1.3"/><path d="M8 10l1.5 1.5L12 8.5" stroke="#fff" stroke-width="1.3" fill="none"/></svg>THERMAL INSPECTION</li>
    <li><svg width="20" height="20" viewBox="0 0 20 20"><circle cx="10" cy="10" r="10" fill="var(--blue-deep)"/><circle cx="6.5" cy="6.5" r="1.8" fill="#fff"/><circle cx="13.5" cy="6.5" r="1.8" fill="#fff"/><circle cx="6.5" cy="13.5" r="1.8" fill="#fff"/><circle cx="13.5" cy="13.5" r="1.8" fill="#fff"/><path d="M7 7l6 6M13 7l-6 6" stroke="#fff" stroke-width="1.2"/></svg>PROJECT FOLLOWING</li>
    <li><svg width="20" height="20" viewBox="0 0 20 20"><circle cx="10" cy="10" r="10" fill="var(--blue-deep)"/><rect x="4.5" y="7" width="8" height="6" rx="1" fill="#fff"/><path d="M12.5 10l3-2v4z" fill="#fff"/></svg>AERIAL PHOTOGRAPHY / VIDEOGRAPHY</li>
  </ul>
  <div class="photo ring" style="left:15px;top:285px;width:124px;height:124px;background:radial-gradient(circle at 45% 45%,#f4d06a,#d8456c 40%,#6b3aa0 70%,#444 100%)" role="img" aria-label="Photo of a tablet showing a thermal image of a building"></div>

  <div class="mining">
    <h3>SERVICE FOR MINING COMPANIES</h3>
    <ul style="left:0">
      <li>Geophysical surveys</li><li>Mapping</li><li>Inspections Visual / thermal</li><li>Power lines</li><li>Pipelines/pipelines</li><li>Railroads</li>
    </ul>
    <ul style="left:118px">
      <li>Services to municipalities</li><li>Planning</li><li>Civil security</li><li>Agricultural</li><li>Mapping</li><li>Volumetry/Photogrammetry</li>
    </ul>
  </div>

  <div class="photo" style="left:335px;top:20px;width:110px;height:100px;border-radius:40%;background:radial-gradient(ellipse at center,#6a6a6c,rgba(60,60,62,0) 70%)" role="img" aria-label="Photo of a hovering quadcopter drone"></div>
  <div class="about">
    <h2 class="title title--light">Drone Division</h2>
    <p>As our drone pilots are also our helicopter pilots, we are able to offer you a multitude of services in several sectors, even in remote areas! All of our pilots have advanced Transport Canada certification and extensive flight experience. Our equipment is certified by Transport Canada and we can operate in all airspace. Day and night, we offer solutions tailored to your needs with fast, state-of-the-art data planning and processing.</p>
  </div>
  <div class="contact">
    <h2 class="title title--light">Contact</h2>
    <p>The main base of Vireo Rotorcraft Ltd<br>Is located at Lakeview airport Québec, Canada.<br>GPS: 48°12'10"N 71°40'20"W</p>
    <p style="margin-top:12px"><strong>e-mail: info@vireorotorcraft.com<br>Phone: 418-555-0142<br>Fax: 418-555-0177</strong></p>
  </div>

  <div class="brand">
    <span class="brand-mark"></span>
    <span class="brand-name"><span class="small">Vireo Rotorcraft</span><span class="big">Division Drones</span></span>
  </div>
  <p class="tagline title title--light">Photography, Videography<br>&amp; Drone Inspection Service</p>
  <div class="url-pill">www.vireorotorcraft.com</div>
</section>

<section class="sheet sheet--inside" aria-label="Brochure inside">
  <svg class="sheet-bg" width="749" height="530" viewBox="0 0 749 530">
    <defs>
      <linearGradient id="darkGrad2" x1="0" y1="0" x2="1" y2="1">
        <stop offset="0" stop-color="#161617"/><stop offset=".5" stop-color="#3e3e40"/><stop offset="1" stop-color="#1a1a1b"/>
      </linearGradient>
      <linearGradient id="paperGrad2" x1="0" y1="0" x2="1" y2="0">
        <stop offset="0" stop-color="#ffffff"/><stop offset="1" stop-color="#e6e6e8"/>
      </linearGradient>
      <linearGradient id="heliGrad" x1="0" y1="0" x2="0" y2="1">
        <stop offset="0" stop-color="#b9c4cf"/><stop offset=".5" stop-color="#6f7d76"/><stop offset="1" stop-color="#3a4a3a"/>
      </linearGradient>
      <linearGradient id="lakeGrad" x1="0" y1="0" x2="0" y2="1">
        <stop offset="0" stop-color="#6f8a55"/><stop offset=".45" stop-color="#8a9aa8"/><stop offset="1" stop-color="#b06a2c"/>
      </linearGradient>
    </defs>
    <rect x="0" y="0" width="250" height="530" fill="url(#darkGrad2)"/>
    <rect x="250" y="0" width="250" height="530" fill="url(#paperGrad2)"/>
    <rect x="500" y="0" width="249" height="530" fill="url(#darkGrad2)"/>
    <path d="M0 360C80 330 170 330 250 350V530H0Z" fill="url(#heliGrad)" role="img" aria-label="Photo of a yellow helicopter and a drone in flight over a forest"/>
    <path d="M0 360C80 330 170 330 250 350V356C170 338 80 338 0 366Z" fill="var(--blue)"/>
    <path d="M500 0H749V110C690 150 590 160 500 150Z" fill="url(#lakeGrad)" role="img" aria-label="Photo of a red helicopter and an inspection drone by a lake in autumn"/>
    <path d="M500 150C590 160 690 150 749 110V122C690 162 590 170 500 160Z" fill="#e8ecf0"/>
    <path d="M500 160C590 170 690 162 749 122V130C690 170 590 178 500 168Z" fill="var(--blue)"/>
    <rect x="322" y="363" width="120" height="104" fill="#fff"/>
    <rect x="322" y="363" width="120" height="40" fill="#9a9485" role="img" aria-label="Aerial map of a stockpile"/>
    <path d="M330 460C350 460 360 455 372 432C380 418 390 418 398 432C410 455 420 460 436 460" fill="#dbe7f6" stroke="var(--blue)" stroke-width="1"/>
    <path d="M330 460H436M330 410V460" stroke="#bbb" stroke-width=".6"/>
  </svg>

  <div class="photogrammetry">
    <h2 class="title title--light">Photogrammetry</h2>
    <div class="title-rule" style="left:20px;top:51px;width:120px"></div>
    <div class="photo" style="left:20px;top:60px;width:106px;height:69px;background:linear-gradient(135deg,#6b7a5c,#a9aba6 50%,#4e5b48)" role="img" aria-label="Aerial photo of a building site"></div>
    <div class="photo" style="left:132px;top:60px;width:106px;height:69px;background:linear-gradient(135deg,#5f6e52,#b0b1ad 50%,#506048)" role="img" aria-label="Aerial photogrammetry model of the same site"></div>
    <p class="lead" style="left:20px;top:146px">Creating map from aerial photographs</p>
    <ul class="ticks">
      <li>Detailed inspection data to the centimeter</li>
      <li>Faster than traditional techniques</li>
      <li>Access to inaccessible or dangerous areas for humans</li>
      <li>Compilation of digital elevation models, contours, volume measurements, etc ...</li>
    </ul>
    <div class="photo ring" style="left:4px;top:278px;width:100px;height:100px;background:radial-gradient(circle,#a7a39b,#6f7b63 70%)" role="img" aria-label="Aerial photo of an open-pit quarry"></div>
  </div>

  <div class="volumetric">
    <h2 class="title">Volumetric</h2>
    <div class="title-rule" style="left:318px;top:51px;width:112px;background:var(--blue)"></div>
    <div class="calc">
      <b>Volume Calculation</b>
      <p>Calculated Volume: 1,565.46 yd³</p>
      <p>Void Volume: 5,534.70 yd³</p>
      <p>Minimum Height: 1,029.56 ft<br>Maximum Height: 1,045.60 ft<br>Area of Measurement: 1406.87 yd²</p>
    </div>
    <div class="photo" style="left:354px;top:75px;width:133px;height:87px;background:radial-gradient(circle at 55% 50%,#c08a5a,#9fa39c 35%,#8a9184)" role="img" aria-label="Aerial map of a gravel pile with the measured area outlined"></div>
    <p class="lead" style="left:266px;top:178px;width:225px;color:#444;line-height:12px">Volumetry calculations of various materials from aerial Photogrammetry</p>
    <ul class="feature-list">
      <li><svg width="26" height="26" viewBox="0 0 26 26"><circle cx="13" cy="13" r="12" fill="var(--blue)" stroke="#d5e3f2" stroke-width="2"/><circle cx="13" cy="13" r="6" fill="none" stroke="#fff" stroke-width="1.4"/><circle cx="13" cy="13" r="2" fill="#fff"/></svg>PRECISION</li>
      <li><svg width="26" height="26" viewBox="0 0 26 26"><circle cx="13" cy="13" r="12" fill="var(--blue)" stroke="#d5e3f2" stroke-width="2"/><path d="M8 12h3v7H8zM11 12l3-5c1.5 0 1.5 2 1 4h3c1 0 1 2 0 2v4c0 1-1 2-2 2h-5z" fill="#fff"/></svg>ECONOMY</li>
      <li><svg width="26" height="26" viewBox="0 0 26 26"><circle cx="13" cy="13" r="12" fill="var(--blue)" stroke="#d5e3f2" stroke-width="2"/><path d="M7 16a6 6 0 0 1 12 0z" fill="#fff"/><path d="M13 16l3-4" stroke="var(--blue)" stroke-width="1.4"/></svg>TIMELINESS</li>
      <li><svg width="26" height="26" viewBox="0 0 26 26"><circle cx="13" cy="13" r="12" fill="var(--blue)" stroke="#d5e3f2" stroke-width="2"/><path d="M13 6l5 2v4c0 4-3 6-5 7-2-1-5-3-5-7V8z" fill="#fff"/></svg>SECURITY</li>
    </ul>
    <div class="table" style="left:260px"><b>Measurements</b>Length 7.72 m<br>Width 7.72 m<br>Min elev 675.27 m<br>Max elev 675.27 m<br>Diff 0.00 m<br>Slope 0.01 %</div>
    <div class="table" style="left:446px"><b>Measurements</b>Length 7.72 m<br>Width 7.72 m<br>Min elev 675.27 m<br>Max elev 675.27 m<br>Diff 0.00 m<br>Slope 0.03 %</div>
  </div>

  <div class="inspection">
    <h2 class="title title--light">Inspection</h2>
    <div class="title-rule" style="left:527px;top:209px;width:105px;background:var(--blue)"></div>
    <p class="lead" style="left:527px;top:214px">Visual or Thermal</p>
  </div>
  <svg class="abs" style="left:500px;top:238px" width="249" height="80" viewBox="0 0 249 80">
    <g fill="none" stroke="#fff" stroke-width="1.6">
      <circle cx="48" cy="16" r="14"/><circle cx="124" cy="16" r="14"/><circle cx="198" cy="16" r="14"/>
      <circle cx="87" cy="62" r="14"/><circle cx="164" cy="62" r="14"/>
    </g>
    <g fill="var(--blue)">
      <circle cx="48" cy="16" r="10"/><circle cx="124" cy="16" r="10"/><circle cx="198" cy="16" r="10"/>
      <circle cx="87" cy="62" r="10"/><circle cx="164" cy="62" r="10"/>
    </g>
    <path d="M42 20a6 6 0 0 1 12 0z" fill="#fff"/>
    <circle cx="124" cy="16" r="5" fill="none" stroke="#fff" stroke-width="1.3"/><circle cx="124" cy="16" r="1.6" fill="#fff"/>
    <path d="M193 11l10 10M203 11l-10 10" stroke="#fff" stroke-width="1.5"/>
    <path d="M87 56l6 10H81z" fill="#fff"/>
    <path d="M158 66a6 6 0 0 1 12 0z" fill="#fff"/>
  </svg>
  <div class="icon-label" style="left:508px;top:276px">SPEED</div>
  <div class="icon-label" style="left:584px;top:276px">PRECISION</div>
  <div class="icon-label" style="left:658px;top:276px">DIFFICULT<br>ACCESS</div>
  <div class="icon-label" style="left:547px;top:327px">DANGEROUS<br>AREAS</div>
  <div class="icon-label" style="left:624px;top:327px">SITE<br>MONITORING</div>

  <div class="photo" style="left:519px;top:355px;width:106px;height:64px;background:linear-gradient(#c9ced4,#9aa0a6 55%,#6f7478)" role="img" aria-label="Wide view of a helicopter on a tarmac"><span class="zoom-tag">1x</span></div>
  <div class="photo" style="left:631px;top:355px;width:106px;height:64px;background:linear-gradient(#b8bcc0,#d4444f 55%,#7d7f82)" role="img" aria-label="Zoomed view of the red helicopter"><span class="zoom-tag">60x</span></div>
  <div class="photo" style="left:519px;top:426px;width:106px;height:64px;background:linear-gradient(#c0c4c8,#c9454e 50%,#6f7276)" role="img" aria-label="Closer view of the red helicopter"><span class="zoom-tag">30x</span></div>
  <div class="photo" style="left:631px;top:426px;width:106px;height:64px;background:linear-gradient(#c4c4c4,#4a4a4c 60%,#8d8d8f)" role="img" aria-label="Close-up of the helicopter rotor hub"><span class="zoom-tag">180x</span></div>

  <div class="footer-bar">
    <span class="phone"><svg width="12" height="12" viewBox="0 0 12 12" style="margin-right:6px"><circle cx="6" cy="6" r="5.3" fill="none" stroke="#fff"/><path d="M4 3.5l1 1-0.6 1c.4.9 1 1.5 1.9 1.9l1-.6 1 1-.8.9c-2 0-4.5-2.5-4.5-4.5z" fill="#fff"/></svg>(418) 555-0142</span>
    <span class="web">www.vireorotorcraft.com</span>
  </div>
</section>

</body>
</html>
```